Edgy rebranded biz cards KRB

We are rebranding our 20 yr old mortgage company with a new logo and would like cards to compliment our new look.

Target Market(s)

potential home buyers or clients for refinance

Industry/Entity Type

Mortgage Brokerage

Contact Information for Business Card

418 W. Lomita Ave #305
Henderson, NV 89152
702.519.4827 o
702-519-4829 f
www.kestrelridgelending,example
nmls 842019
KRB is an equal housing lender

Font styles to use
Sans Serif

Colors
0455a3
3176b5
0393ce
33a6d7

Requirements
Must have
• space for a photo
Nice to have
• One side with the company info and the other with the person's info

```html
<!DOCTYPE html>
<html lang="en">
<head>
<meta charset="utf-8">
<title>Kestrel Ridge Lending – Business Cards</title>
<link href="https://fonts.googleapis.com/css2?family=Fira+Sans:wght@300;400;600&display=swap" rel="stylesheet">
<style>
  :root {
    --brand-blue: #2782fc;
    --brand-blue-soft: #cfe2fe;
    --ink-grey: #6e7073;
    --icon-grey: #6b6d70;
    --paper: #ffffff;
    --stage: #ffffff;
  }
  * { margin: 0; padding: 0; box-sizing: border-box; }
  html, body { width: 1200px; height: 1000px; overflow: hidden; background: var(--stage); }
  body { position: relative; font-family: "Fira Sans", Arial, sans-serif; }

  .card {
    position: absolute;
    left: 233px;
    width: 735px;
    height: 420px;
    box-shadow: 3px 4px 7px rgba(0,0,0,0.28);
    overflow: hidden;
  }
  .card--front { top: 45px; background: var(--brand-blue); color: var(--paper); text-align: center; }
  .card--back { top: 535px; background: var(--paper); }

  /* Front */
  .front-brand {
    position: absolute; left: 0; right: 0; top: 110px;
    font-weight: 600; font-size: 58px; line-height: 1.05; letter-spacing: 1px;
  }
  .front-brand span { display: block; }
  .front-tagline {
    position: absolute; left: 0; right: 0; top: 287px;
    font-weight: 600; font-size: 32px; letter-spacing: 0.3px;
  }
  .front-web {
    position: absolute; left: 0; right: 0; top: 336px;
    font-weight: 300; font-size: 23px; letter-spacing: 0.6px;
  }

  /* Back */
  .back-art { position: absolute; inset: 0; }
  .back-brand {
    position: absolute; left: 405px; width: 280px; top: 55px;
    text-align: center; color: var(--brand-blue);
    font-weight: 600; font-size: 36px; line-height: 1.08;
  }
  .back-brand span { display: block; }
  .nmls {
    position: absolute; left: 409px; top: 204px;
    color: var(--brand-blue); font-size: 17px;
  }
  .contact-list { position: absolute; left: 366px; top: 256px; list-style: none; }
  .contact-item {
    display: flex; align-items: flex-start; gap: 14px;
    color: var(--brand-blue); font-size: 20px; line-height: 25px; margin-bottom: 7px;
  }
  .contact-item svg { flex: none; width: 29px; height: 25px; fill: var(--icon-grey); }
  .person {
    position: absolute; left: 0; width: 348px; top: 270px; text-align: center;
  }
  .person-name { color: var(--brand-blue); font-weight: 600; font-size: 27px; letter-spacing: 0.3px; }
  .person-role { color: var(--ink-grey); font-weight: 400; font-size: 19px; margin-top: 6px; }
</style>
</head>
<body>

<section class="card card--front">
  <div class="front-brand"><span>KESTREL RIDGE</span><span>LENDING</span></div>
  <div class="front-tagline">EQUAL HOUSING LENDER</div>
  <div class="front-web">www.kestrelridgelending.example</div>
</section>

<section class="card card--back">
  <svg class="back-art" viewBox="0 0 735 420" width="735" height="420">
    <polygon points="0,0 147,0 0,125" fill="var(--brand-blue)"/>
    <polyline points="0,145 139,20 325,177 325,213" fill="none" stroke="var(--brand-blue)" stroke-width="5"/>
    <rect x="77" y="50" width="130" height="160" rx="14" fill="var(--brand-blue-soft)" role="img" aria-label="Portrait photo of the loan officer"/>
    <polygon points="0,202 325,209 392,214 0,228" fill="var(--brand-blue)"/>
    <polygon points="735,300 735,420 588,420" fill="var(--brand-blue)"/>
    <line x1="735" y1="280" x2="568" y2="420" stroke="var(--brand-blue)" stroke-width="5"/>
  </svg>

  <div class="back-brand"><span>KESTREL RIDGE</span><span>LENDING</span></div>
  <div class="nmls">Company NMLS 842019</div>

  <ul class="contact-list">
    <li class="contact-item">
      <svg viewBox="0 0 29 25"><path d="M14.5 3 L1 14 L4 14 L14.5 6 L25 14 L28 14 Z M6 14 L6 19 L23 19 L23 14 L14.5 8 Z"/></svg>
      <span>418 W. Lomita Ave #305<br>Henderson, NV 89152</span>
    </li>
    <li class="contact-item">
      <svg viewBox="0 0 29 25"><path d="M5 2 Q3 3 3 6 Q5 15 13 21 Q17 24 21 23 Q23 22 24 20 L20 16 Q18 17 17 18 Q12 15 9 9 Q11 8 11 6 L7 2 Z"/></svg>
      <span>702-519-4827</span>
    </li>
    <li class="contact-item">
      <svg viewBox="0 0 29 25"><rect x="7" y="2" width="15" height="6"/><rect x="2" y="9" width="25" height="10" rx="2"/><rect x="7" y="16" width="15" height="7" fill="#fff" stroke="var(--icon-grey)" stroke-width="2"/></svg>
      <span>702-519-4829</span>
    </li>
  </ul>

  <div class="person">
    <div class="person-name">PLACE FOR NAME</div>
    <div class="person-role">Owner</div>
  </div>
</section>

</body>
</html>
```